Horse related business entrepreneur needs a business card

I need a business card design for my horse related business. The enterprise is Tall Fern LLC and I have 3 businesses (headquartered at 2 locations): 1. property management where we rent horse stalls and apartments at a thoroughbred training center outside Ocala; 2. a medium sized transportation service in central Florida that sells horse bedding and removes used horse bedding from horse farms; and horse racing

```html
<!DOCTYPE html>
<html lang="en">
<head>
<meta charset="utf-8">
<title>Tall Fern Farm — Business Card</title>
<link rel="stylesheet" href="https://fonts.googleapis.com/css2?family=Cinzel:wght@500&family=Lato:wght@400&display=swap">
<style>
  :root {
    --backdrop: #2b2b2b;
    --card-dark: #050505;
    --card-light: #f7f7f5;
    --teal: #1f5b78;
    --orange: #e0804a;
    --ink-light: #ffffff;
  }
  html, body {
    margin: 0;
    padding: 0;
    width: 1200px;
    height: 900px;
    overflow: hidden;
    background: var(--backdrop);
  }
  .canvas {
    position: relative;
    width: 1200px;
    height: 900px;
  }
  .card {
    position: absolute;
    left: 340px;
    width: 520px;
    height: 298px;
    border-radius: 22px;
    box-shadow: 0 18px 40px rgba(0,0,0,0.55);
    font-family: "Lato", Arial, sans-serif;
  }
  .card--back { top: 100px; background: var(--card-dark); color: var(--ink-light); }
  .card--front { top: 500px; background: var(--card-light); }

  .brand {
    position: absolute;
    display: flex;
    align-items: center;
    gap: 10px;
    font-family: "Cinzel", Georgia, serif;
    font-weight: 500;
    letter-spacing: 2px;
    white-space: nowrap;
    color: var(--teal);
  }
  .brand__dot { width: 12px; height: 12px; border-radius: 50%; flex: none; }
  .card--back .brand { left: 50%; top: 118px; transform: translateX(-50%); font-size: 28px; }
  .card--back .brand__dot { background: var(--teal); }
  .card--front .brand { right: 32px; top: 40px; font-size: 22px; }
  .card--front .brand__dot { background: var(--orange); }

  .address {
    position: absolute;
    display: flex;
    align-items: flex-end;
    gap: 6px;
    font-size: 13px;
    line-height: 1.35;
    font-style: normal;
  }
  .address svg { width: 10px; height: 14px; flex: none; margin-bottom: 2px; }
  .address--primary { left: 28px; bottom: 28px; }
  .address--secondary { right: 28px; top: 40px; text-align: right; flex-direction: row-reverse; align-items: flex-start; }
  .address--secondary svg { margin-top: 2px; }

  .person { position: absolute; left: 40px; top: 104px; }
  .person__name {
    font-family: "Cinzel", Georgia, serif;
    font-weight: 500;
    font-size: 22px;
    letter-spacing: 1px;
    color: var(--teal);
    margin: 0;
    line-height: 1.1;
  }
  .person__role { font-size: 15px; color: var(--orange); margin: 2px 0 0; }

  .contact-list {
    position: absolute;
    left: 60px;
    top: 168px;
    margin: 0;
    padding: 0;
    list-style: none;
    font-size: 14px;
    line-height: 22px;
    color: var(--teal);
  }
  .contact-list li { display: flex; align-items: center; gap: 8px; }
  .contact-list svg { width: 13px; height: 11px; fill: var(--orange); flex: none; }

  .website { position: absolute; left: 60px; bottom: 26px; margin: 0; font-size: 15px; color: var(--orange); }
</style>
</head>
<body>
<main class="canvas">

  <section class="card card--back" aria-label="Card back">
    <div class="brand"><span class="brand__dot"></span>Tall Fern Farm</div>

    <address class="address address--secondary">
      <svg viewBox="0 0 10 14" aria-hidden="true"><path d="M5 0a5 5 0 0 0-5 5c0 3.5 5 9 5 9s5-5.5 5-9a5 5 0 0 0-5-5zm0 7a2 2 0 1 1 0-4 2 2 0 0 1 0 4z" fill="var(--teal)"/></svg>
      <span>718 Willow Ridge Lane<br>Crozet, VA 22932</span>
    </address>

    <address class="address address--primary">
      <svg viewBox="0 0 10 14" aria-hidden="true"><path d="M5 0a5 5 0 0 0-5 5c0 3.5 5 9 5 9s5-5.5 5-9a5 5 0 0 0-5-5zm0 7a2 2 0 1 1 0-4 2 2 0 0 1 0 4z" fill="var(--teal)"/></svg>
      <span>1420 SE 92nd Court<br>Dunnellon, FL 34431</span>
    </address>
  </section>

  <section class="card card--front" aria-label="Card front">
    <div class="brand"><span class="brand__dot"></span>Tall Fern Farm</div>

    <div class="person">
      <p class="person__name">Owen Carlisle</p>
      <p class="person__role">Owner</p>
    </div>

    <ul class="contact-list">
      <li>
        <svg viewBox="0 0 13 11" aria-hidden="true"><path d="M0 1h13v9H0z"/><path d="M0 1l6.5 5L13 1" stroke="var(--card-light)" stroke-width="1.2" fill="none"/></svg>
        owen@tallfern.com
      </li>
      <li>
        <svg viewBox="0 0 13 11" aria-hidden="true"><path d="M1 3c0-2 11-2 11 0v1.5H9.5V3h-6v1.5H1z"/><path d="M3 5h7l1.5 5h-10z"/></svg>
        (434) 555-0148
      </li>
      <li>
        <svg viewBox="0 0 13 11" aria-hidden="true"><path d="M3 0h6v3H3z"/><path d="M0 3.5h13V11H0z"/><path d="M2.5 6h8M2.5 8h8" stroke="var(--card-light)" stroke-width="1"/></svg>
        (434) 555-0192
      </li>
    </ul>

    <p class="website">www.tallfern.com</p>
  </section>

</main>
</body>
</html>
```